Pebble nook day nursery qrv limited

we would like create a website that can be updated by us easily as we have regular changes to what we provide and need. we would like something that is classy but also appealing from a child's aspect. we would be looking to add our own logo and our edvarin logo both attached, if you guys can create it and we will work with the preferred choice to add all the text.
We would like the links to kin pathways, edvarin report and our chatterloom feed on the front page

we are looking for a website for our childcare business we have 2 nurseries that we would like one website.
showing our opening hours, price list, policies etc as well as photos, description of our day, staff photos and their training accreditation's.

Target Market(s)

Families

Industry/Entity Type

Childcare

Number of Pages Required

5+ page

Font styles to use
Serif

Colors

Designer to choose colors to be used in the design.

Requirements
Must have
• links to social media and other websites, photographs, links to download registration forms etc, parents able to leave reviews. wayrund plots link, job opportunities
Nice to have
• facilities to take payments

```html
<!DOCTYPE html>
<html lang="en">
<head>
<meta charset="utf-8">
<title>Pebble Nook Day Nursery</title>
<link href="https://fonts.googleapis.com/css2?family=Roboto:wght@300;400;500;700;900&family=Roboto+Condensed:wght@400;700&family=Raleway:wght@400;600;700&display=swap" rel="stylesheet">
<style>
:root{
  --green:#5bb346;
  --green-dark:#3f9a2f;
  --pink:#d6247f;
  --pink-deep:#b81a6b;
  --navy:#1f3d7a;
  --blue:#3a8fd0;
  --blue-pale:#e6f3fc;
  --blue-row:#d2eafa;
  --slate:#3a4556;
  --ink:#444a55;
  --grey:#f2f3f5;
  --white:#fff;
}
*{margin:0;padding:0;box-sizing:border-box}
html,body{width:1200px;height:4054px;overflow:hidden}
body{font-family:"Roboto",sans-serif;color:var(--ink);background:var(--white);position:relative}
section,header,footer,div{position:relative}
.abs{position:absolute}
.fill{position:absolute}

/* top bar */
.topbar{height:22px;background:var(--green);color:#fff;font-size:10px;display:flex;justify-content:flex-end;align-items:center;gap:26px;padding-right:180px}
.topbar span::before{content:"";display:inline-block;width:7px;height:7px;background:#fff;border-radius:2px;margin-right:5px;vertical-align:-1px}

/* header */
.header{height:92px;background:var(--white)}
.brand{position:absolute;left:160px;top:10px;width:150px;text-align:center}
.brand-mark{width:26px;height:26px;border-radius:50%;background:var(--green);margin:0 auto 4px}
.brand-name{font-family:"Roboto",sans-serif;font-weight:700;font-size:15px;color:var(--navy);line-height:1.1}
.socials{position:absolute;left:886px;top:30px;display:flex;gap:14px}
.socials i{width:30px;height:30px;border:2px solid var(--blue);border-radius:50%;display:block}

/* hero */
.hero{height:529px;overflow:hidden}
.hero-photo{inset:0;background:linear-gradient(180deg,#9bb8cf 0%,#c0a48a 45%,#d56f55 80%,#8d5a3e 100%)}
.nav{position:absolute;left:176px;top:6px;width:870px;height:38px;background:rgba(214,36,127,.88);display:flex;align-items:center;justify-content:space-between;padding:0 10px}
.nav a{color:#fff;text-decoration:none;font-family:"Roboto Condensed",sans-serif;font-size:14px;font-weight:700;padding:10px 16px;text-transform:uppercase}
.nav a.active{background:var(--pink-deep)}
.hero-title{position:absolute;width:100%;text-align:center;top:222px}
.hero-title .light{font-family:"Raleway",sans-serif;font-size:40px;color:#fff;letter-spacing:1px}
.hero-title .bold{font-family:"Roboto",sans-serif;font-weight:900;font-size:58px;color:var(--pink);line-height:1.05}
.arrows{position:absolute;top:340px;left:0;width:100%;display:flex;justify-content:center;gap:6px}
.arrows i{width:18px;height:18px;border:1px solid #fff;display:block;background:rgba(0,0,0,.2)}

/* welcome */
.welcome{height:200px;background:var(--slate);text-align:center;color:#fff}
.welcome h2{padding-top:28px;font-family:"Raleway",sans-serif;font-weight:600;font-size:32px}
.welcome h1{font-family:"Roboto",sans-serif;font-weight:700;font-size:38px;color:var(--green);letter-spacing:1px}
.welcome p{width:860px;margin:18px auto 0;font-size:11px;line-height:1.5;color:#dfe3ea}

/* prices */
.prices{height:644px;text-align:center;background:#fbfbfc}
.prices h2{padding-top:38px;font-weight:700;font-size:34px;color:var(--navy)}
.prices .sub{font-size:14px;color:var(--pink);margin-top:4px;letter-spacing:.5px}
.price-table{position:absolute;left:160px;top:126px;width:878px;border-collapse:collapse}
.price-table th{background:var(--blue);color:#fff;font-weight:400;font-size:22px;height:44px;text-align:left;padding-left:30px;border:2px solid var(--white)}
.price-table th:nth-child(n+2){text-align:center;padding:0}
.price-table td{height:89px;border:2px solid var(--white);background:var(--blue-pale);color:var(--navy);font-size:28px;text-align:center}
.price-table tr:nth-child(even) td{background:var(--blue-row)}
.price-table td:first-child{text-align:left;padding-left:30px;width:262px}
.price-table td:nth-child(2){width:340px}
.price-table .day{font-size:26px;display:block;line-height:1.1}
.price-table small{display:block;font-size:14px;line-height:1.2}
.price-table .note{font-size:13px;display:block;color:var(--blue)}
.meals{position:absolute;top:555px;width:100%;font-size:15px;color:#777}
.funding{position:absolute;top:586px;width:100%;font-size:22px;font-weight:500;color:var(--pink);letter-spacing:.5px}

/* our day */
.ourday-head{height:143px;background:var(--pink);text-align:center;color:#fff}
.ourday-head h2{padding-top:24px;font-size:32px;font-weight:700}
.divider{display:flex;align-items:center;justify-content:center;gap:8px;margin:6px auto}
.divider::before,.divider::after{content:"";height:2px;width:200px;background:currentColor;opacity:.6}
.divider b{font-size:13px;letter-spacing:4px}
.ourday-head p{width:840px;margin:8px auto 0;font-size:11px;line-height:1.5}
.ourday-grid{height:524px}
.tile{position:absolute}
.tile-main{left:0;top:0;width:584px;height:524px;background:linear-gradient(160deg,#a7794f,#6a4a36 55%,#3e3434)}
.tile-main .shade{position:absolute;inset:0;background:rgba(0,0,0,.35)}
.tile-main .copy{position:absolute;left:42px;top:176px;width:510px;color:#fff}
.tile-main h3{font-size:34px;font-weight:700}
.tile-main h4{font-size:13px;font-weight:400;margin:2px 0 12px;letter-spacing:.3px}
.tile-main p{font-size:12px;line-height:1.5}
.btn{display:inline-block;margin:16px 0 0 50px;background:var(--green);color:#fff;font-size:13px;padding:8px 16px;border-radius:4px}
.tile-text{display:flex;flex-direction:column;justify-content:center;align-items:center;color:#fff;text-align:center}
.tile-text span{font-size:28px;font-weight:300}
.tile-text strong{font-size:38px;font-weight:900;line-height:1}

/* team */
.team{height:541px;text-align:center}
.team h2{padding-top:40px;font-size:32px;font-weight:700;color:var(--pink)}
.team .divider{color:var(--navy)}
.team .divider::before,.team .divider::after{background:#ccc;opacity:1;width:280px}
.team p.intro{width:860px;margin:12px auto 0;font-size:11px;line-height:1.5;color:#888}
.card{position:absolute;top:181px;width:243px;height:333px}
.card .photo{position:absolute;inset:0}
.card .tabs{position:absolute;right:0;top:8px;display:flex;flex-direction:column;gap:4px}
.card .tabs i{width:26px;height:26px;background:#e53935;display:block}
.card .label{position:absolute;left:0;bottom:28px;background:#2e3440;color:#fff;text-align:left;padding:6px 12px;width:150px}
.card .label b{font-size:12px;display:block}
.card .label span{font-size:10px;color:#bbb}

/* report + feed */
.report{height:408px;background:var(--grey);border-top:4px solid var(--pink)}
.report-left{position:absolute;left:0;top:0;width:584px;height:404px;background:linear-gradient(90deg,#e9dfd3,#f1ece6);padding:40px 0 0 160px}
.report-left h2{font-size:30px;font-weight:900;color:var(--pink)}
.report-left h2 em{font-style:normal;color:var(--navy)}
.report-left p{width:400px;font-size:11px;line-height:1.5;margin-top:10px;color:#555}
.badge{position:absolute;left:160px;top:308px;width:64px;height:70px;background:var(--navy);border-radius:4px}
.feed-head{position:absolute;left:600px;top:14px;display:flex;align-items:center;gap:10px}
.feed-head i{width:34px;height:34px;background:var(--blue);display:block}
.feed-head h2{font-size:26px;font-weight:900;color:var(--navy)}
.feed-card{position:absolute;left:600px;top:62px;width:449px;height:332px;background:#fff;padding:16px 20px}
.feed-card .hide{font-size:13px;color:#333;display:flex;align-items:center;gap:10px;font-weight:500}
.feed-card .hide i{width:22px;height:22px;border-radius:50%;background:var(--blue);display:block}
.feed-card p{font-size:10px;margin-top:10px;line-height:1.4;color:#666}
.thumbs{display:grid;grid-template-columns:repeat(4,80px);gap:22px 24px;margin:18px 0 0 12px}
.thumbs div{height:70px;background:linear-gradient(135deg,#b79a86,#6b5a52)}
.thumbs small{display:block;font-size:8px;color:#999;text-align:center;margin-top:4px}

/* reviews */
.reviews{height:511px;text-align:center}
.reviews h2{padding-top:50px;font-size:30px;font-weight:700;color:var(--pink)}
.reviews .divider{color:var(--navy)}
.reviews .divider::before,.reviews .divider::after{background:#ccc;opacity:1;width:280px}
.avatar{width:90px;height:90px;border-radius:50%;border:3px solid var(--pink);margin:18px auto 0;background:linear-gradient(135deg,#e3b8a0,#7e5c4b)}
.quote{position:absolute;font-size:140px;color:#dcdcdc;font-family:Georgia,serif;line-height:1}
.reviews blockquote{width:720px;margin:20px 0 0 346px;text-align:left;font-size:16px;line-height:1.55;color:#666}
.reviewer{position:absolute;left:346px;top:377px;text-align:left}
.reviewer b{font-weight:400;color:var(--pink);font-size:16px;display:block}
.reviewer span{font-size:12px;color:#888}
.dots{position:absolute;left:346px;top:428px;display:flex;gap:6px}
.dots i{width:11px;height:11px;border-radius:50%;border:1px solid #999;display:block}
.dots i:first-child{background:var(--pink);border-color:var(--pink)}

/* footer */
.footer{height:354px;background:linear-gradient(135deg,#4a4e63,#3d4155)}
.hours-box{position:absolute;left:168px;top:-14px;width:224px;height:368px;background:var(--pink);color:#fff;padding:14px 10px}
.hours-box h3{font-size:18px;font-weight:500;border-bottom:1px solid rgba(255,255,255,.5);padding-bottom:6px;margin-bottom:8px}
.hours-box p{font-size:13px;line-height:1.6}
.hours-box .small{font-size:10px;line-height:1.4;margin-bottom:6px}
.pay{border:1px solid rgba(255,255,255,.6);padding:6px;margin-top:12px;text-align:center}
.pay b{font-size:13px;display:block;margin-bottom:6px}
.pay span{display:inline-block;background:#fff;color:var(--navy);font-size:9px;font-weight:700;padding:5px 6px;margin:0 2px}
.contact{position:absolute;left:405px;top:96px;width:633px;color:#fff}
.contact h2{font-size:28px;font-weight:400;margin-bottom:10px}
.fields{display:flex;gap:14px}
.fields div{height:30px;background:#e9eaed;font-size:11px;color:#666;padding:9px 8px}
.textarea{margin-top:10px;height:98px;background:#e9eaed;font-size:11px;color:#666;padding:8px}
.send{position:absolute;right:0;top:290px;background:var(--green);color:#fff;font-size:17px;padding:8px 18px;border-radius:18px;font-weight:500}
.bottom{height:86px;background:var(--green);text-align:center;color:#fff}
.bottom .icons{display:flex;justify-content:center;gap:10px;padding-top:20px}
.bottom .icons i{width:24px;height:24px;border-radius:50%;background:#fff;display:block}
.bottom small{display:block;margin-top:12px;font-size:10px;letter-spacing:1px}
</style>
</head>
<body>

<div class="topbar"><span>Job Opportunities</span><span>Download Registration Forms</span><span>hello@pebblenook.example</span></div>

<header class="header">
  <div class="brand"><div class="brand-mark"></div><div class="brand-name">Pebble Nook<br>Day Nursery</div></div>
  <div class="socials"><i></i><i></i><i></i><i></i></div>
</header>

<section class="hero">
  <div class="fill hero-photo" role="img" aria-label="Photo of children's hands painted in bright colours raised together"></div>
  <nav class="nav">
    <a class="active">Homepage</a><a>Kin Pathways</a><a>Edvarin Report</a><a>Chatterloom Feed</a><a>Child Care</a><a>Team</a><a>Contact Us</a>
  </nav>
  <div class="hero-title"><div class="light">WE WILL TAKE</div><div class="bold">WE WILL TAKE</div></div>
  <div class="arrows"><i></i><i></i></div>
</section>

<section class="welcome">
  <h2>Welcome to</h2>
  <h1>PEBBLE NOOK DAY NURSERY</h1>
  <p>Lorem Ipsum is simply dummy text of the printing and typesetting industry. Lorem Ipsum has been the industry's standard dummy text ever since the 1500s, when an unknown printer took a galley of type and scrambled it to make a type specimen book. It has survived not only five centuries, but also the leap into electronic typesetting, remaining essentially unchanged.</p>
</section>

<section class="prices">
  <h2>NEW PRICE LIST FROM 1ST APRIL 2017</h2>
  <div class="sub">FEES INCLUDE BREAKFAST (FULL DAY/FULL TIME ONLY)</div>
  <table class="price-table">
    <tr><th>DAY</th><th>UNDER 2'S</th><th>2-5'S</th></tr>
    <tr><td><span class="day">HALF DAY</span><small>8AM-1PM OR 1PM-6PM</small></td><td>£26</td><td>£25</td></tr>
    <tr><td><span class="day">FULL DAY</span><small>7.30-6PM</small></td><td>£40</td><td>£38</td></tr>
    <tr><td><span class="day">FULL TIME</span><small>MON - FRI 7.30-6PM</small></td><td>£168</td><td>£161<span class="note">Funded children in holidays</span></td></tr>
    <tr><td><span class="day">FULL TIME</span><small>FUNDED CHILDREN<br>3+ YEARS OLD+</small></td><td style="font-size:14px">XXXXXXXXXXX</td><td>£130<span class="note">During term time</span></td></tr>
  </table>
  <div class="meals">Meals can be offered for an additional charge (£2.50 per meal, per day) Please see a member of staff!</div>
  <div class="funding">IS YOU CHILD ENTITLED TO FUNDING?</div>
</section>

<section class="ourday-head">
  <h2>OUR DAY</h2>
  <div class="divider"><b>★★★</b></div>
  <p>Lorem Ipsum is simply dummy text of the printing and typesetting industry. Lorem Ipsum has been the industry's standard dummy text ever since the 1500s, when an unknown printer took a galley of type and scrambled it to make a type specimen book.</p>
</section>

<section class="ourday-grid">
  <div class="tile tile-main" role="img" aria-label="Photo of a young child playing with colourful toys">
    <div class="shade"></div>
    <div class="copy">
      <h3>LOREM IPSUM IS SIMPLY...</h3>
      <h4>LOREM IPSUM IS SIMPLY DUMMY TEXT OF THE PRINTING</h4>
      <p>Lorem Ipsum is simply dummy text of the printing and typesetting industry. Lorem Ipsum has been the industry's standard dummy text ever since the 1500s, when an unknown printer took a galley of type and scrambled it to make a type specimen book.</p>
      <span class="btn">● Read More...</span>
    </div>
  </div>
  <div class="tile" style="left:584px;top:0;width:308px;height:257px;background:linear-gradient(135deg,#f1d4b8,#e9a66f 60%,#c78a5a)" role="img" aria-label="Photo of a child showing hands painted with smiling faces"></div>
  <div class="tile tile-text" style="left:892px;top:0;width:308px;height:257px;background:var(--navy)"><span>LOREM IPSUM</span><strong>SIMPLY DUMMY</strong></div>
  <div class="tile tile-text" style="left:584px;top:257px;width:308px;height:267px;background:var(--green)"><span>LOREM IPSUM</span><strong>SIMPLY DUMMY</strong></div>
  <div class="tile" style="left:892px;top:257px;width:308px;height:267px;background:linear-gradient(135deg,#e8e2d6,#d9a87c 55%,#b8c6d8)" role="img" aria-label="Photo of a child painting a rainbow on an easel"></div>
</section>

<section class="team">
  <h2>OUR TEAM</h2>
  <div class="divider"><b>★★★</b></div>
  <p class="intro">Lorem Ipsum is simply dummy text of the printing and typesetting industry. Lorem Ipsum has been the industry's standard dummy text ever since the 1500s, and more recently with desktop publishing software including many versions of Lorem Ipsum.</p>
  <div class="card" style="left:173px">
    <div class="photo" style="background:linear-gradient(180deg,#c48e66,#4a3a36 60%,#23262e)" role="img" aria-label="Staff portrait photo"></div>
    <div class="tabs"><i></i><i></i><i></i></div>
    <div class="label"><b>OWEN PARDELL</b><span>Lorem ipsum is simply</span></div>
  </div>
  <div class="card" style="left:484px">
    <div class="photo" style="background:linear-gradient(180deg,#d7c8b8,#e7a9b5 55%,#9b8a80)" role="img" aria-label="Staff portrait photo"></div>
    <div class="tabs"><i></i><i></i><i></i></div>
    <div class="label"><b>LENA BRACKWELL</b><span>Lorem ipsum is simply</span></div>
  </div>
  <div class="card" style="left:784px">
    <div class="photo" style="background:linear-gradient(180deg,#b7937a,#d8c4b0 55%,#8d7766)" role="img" aria-label="Staff portrait photo"></div>
    <div class="tabs"><i></i><i></i><i></i></div>
    <div class="label"><b>SIMON FARROWBY</b><span>Lorem ipsum is simply</span></div>
  </div>
</section>

<section class="report">
  <div class="report-left" role="img" aria-label="Faded photo of a child playing behind the report text">
    <h2>EDVARIN <em>REPORT:</em></h2>
    <p>Lorem Ipsum is simply dummy text of the printing and typesetting industry. Lorem Ipsum has been the industry's standard dummy text ever since the 1500s, when an unknown printer took a galley of type and scrambled it to make a type specimen book. It has survived not only five centuries, but also the leap into electronic typesetting, remaining essentially unchanged.</p>
    <p>Lorem Ipsum is simply dummy text of the printing and typesetting industry. Lorem Ipsum has been the industry's standard dummy text ever since the 1500s, when an unknown printer took a galley of type and scrambled it to make a type specimen book. It has survived not only five centuries, but also the leap into electronic typesetting, remaining essentially unchanged. It was popularised in the 1960s with the release of sheets containing Lorem Ipsum passages.</p>
  </div>
  <div class="badge"></div>
  <div class="feed-head"><i></i><h2>CHATTERLOOM FEED:</h2></div>
  <div class="feed-card">
    <div class="hide"><i></i>Unfollow people to hide their posts</div>
    <p>Lorem ipsum is simply dummy text of the printing and typesetting industry. Lorem Ipsum has been the industry's...</p>
    <div class="thumbs" role="img" aria-label="Grid of eight small photos from the feed">
      <div></div><div></div><div></div><div></div>
      <div></div><div></div><div></div><div></div>
    </div>
  </div>
</section>

<section class="reviews">
  <h2>PARENTS REVIEWS</h2>
  <div class="divider"><b>★★★</b></div>
  <div class="avatar" role="img" aria-label="Round photo of the reviewing parent with child"></div>
  <div class="quote" style="left:210px;top:215px">“</div>
  <div class="quote" style="left:860px;top:370px">”</div>
  <blockquote>Lorem Ipsum is simply dummy text of the printing and typesetting industry. Lorem Ipsum has been the industry's standard dummy text ever since the 1500s, when an unknown printer took a galley of type and scrambled it to make a type specimen book.</blockquote>
  <div class="reviewer"><b>Hattie Quillon</b><span>Happy client</span></div>
  <div class="dots"><i></i><i></i><i></i></div>
</section>

<footer class="footer" role="img" aria-label="Muted street map background behind the contact area">
  <div class="hours-box">
    <h3>Opening Hour</h3>
    <p>Monday - Friday 9am to 5pm<br>Saturday - Sunday off</p>
    <h3 style="margin-top:12px">About Pebble Nook</h3>
    <p class="small">Lorem Ipsum is simply dummy text of the printing and typesetting industry. Lorem Ipsum has been the standard dummy text ever since the 1500s, when an unknown printer took a galley.</p>
    <p class="small">Lorem Ipsum is simply dummy text of the printing and typesetting industry. Lorem Ipsum has been the standard dummy text.</p>
    <div class="pay"><b>Our Payment Methods:</b><span>Cardmo</span><span>Paylink</span><span>Tapro</span><span>Cardmo</span></div>
  </div>
  <div class="contact">
    <h2>Contact Us</h2>
    <div class="fields"><div style="width:149px">Name:</div><div style="width:224px">Phone Number</div><div style="width:232px">eMail</div></div>
    <div class="textarea">Your Comments:</div>
  </div>
  <div class="send" style="left:938px;right:auto;top:286px">Send Us</div>
</footer>

<div class="bottom">
  <div class="icons"><i></i><i></i><i></i></div>
  <small>ALL RIGHT RESERVED 2017</small>
</div>

</body>
</html>
```